Business Card: RW Office Partners - Your tidy answer finder

Business Name: RW Office Partners
Website: www.rwofficepartners.com.au
Email: marisol@rwofficepartners.com.au
Mobile: 61 487 902 346
Facebook: @rwofficepartners
Instrgram: @rwofficepartners

Brading Colours:
HEX
#986474
#ddccd3
#7a8498
#c9d8e4
#000000
#ffffff

Tag Line: Your organised problem solver

Link to DRAFT website:
https://helpdeskhub.sitebuilderx.com/rw-office-partners

About Page from the website:
My name is Marisol Bramwell, and I would love to assist you to become more productive in your day to day and achieve your business and personal goals.
My mission is to give you time, time to work on the important tasks of your business or to be able to spend more time with your family. I will take on the tasks you don’t have time for, don’t know well or simply don’t like to do.
I have an extensive background in Administration, Tender Coordination, Document Control, WHS and Quality Management working primarily in the Construction, Mining and Corporate World.
I am passionate about being organised, having order and making things in your life (and mine) easier! I love to watch something unfold and grow into something amazing! I am known for being the go-to problem solver, the organiser of all things, producing high standards of work even under pressure. I’m also a confident communicator, and I understand that you’re busy running your business.

Target Market(s)

Small to Medium Business who require assistance in their business by a virtual assistant.

Industry/Entity Type

Virtual Assistant

Contact Information for Business Card

Mobile: 61 487 902 346

Font styles to use
Sans Serif

Colors
ffffff

Requirements
Must have
• Branding Colours as outlined.
Contact Details as outlined.
Logo as provided.
Proper contact details - mobile, facebook, instragm, website.
Simple, Elegant, very clean looking.
Should not have
• Note cute with pictures.
Not too girly as still want to market to construction companies.

```html
<!DOCTYPE html>
<html lang="en">
<head>
<meta charset="utf-8">
<title>RW Office Partners – Business Card</title>
<link rel="stylesheet" href="https://fonts.googleapis.com/css2?family=Montserrat:wght@400;500;600&display=swap">
<style>
  :root {
    --mauve: #986474;
    --blush: #ddccd3;
    --slate: #7a8498;
    --mist: #c9d8e4;
    --ink: #000000;
    --paper: #ffffff;
    --backdrop: #eceef1;
  }
  * { box-sizing: border-box; margin: 0; padding: 0; }
  html, body {
    width: 1200px; height: 913px; overflow: hidden;
    background: var(--backdrop);
    font-family: "Montserrat", sans-serif;
  }
  .sheet {
    width: 1200px; height: 913px;
    display: flex; align-items: center; justify-content: center; gap: 40px;
  }
  .card {
    position: relative;
    width: 540px; height: 309px;
    background: var(--paper);
    border-radius: 16px;
    overflow: hidden;
    box-shadow: 0 6px 18px rgba(40, 50, 70, .14);
  }
  .card-band {
    position: absolute; left: 0; bottom: 0;
    width: 100%; height: 40px; display: block;
  }
  .band-main { fill: var(--mauve); }
  .band-accent { fill: var(--blush); }

  /* front */
  .front-brand {
    position: absolute; left: 0; right: 0; top: 108px;
    display: flex; align-items: center; justify-content: center; gap: 14px;
  }
  .brand-dot {
    width: 14px; height: 14px; background: var(--mauve);
  }
  .brand-name {
    color: var(--mauve);
    font-weight: 600;
    text-transform: uppercase;
    letter-spacing: .02em;
    line-height: 1.05;
  }
  .front-brand .brand-name { font-size: 38px; }

  /* back */
  .back-layout {
    position: absolute; left: 34px; top: 88px;
    display: flex; align-items: center; gap: 20px;
  }
  .back-brand { width: 176px; }
  .back-brand .brand-name { font-size: 21px; }
  .tagline {
    margin-top: 6px;
    font-size: 8.5px; font-weight: 500;
    color: var(--slate); text-transform: uppercase; letter-spacing: .03em;
  }
  .divider { width: 2px; height: 124px; background: var(--mauve); }
  .contact-list { list-style: none; display: flex; flex-direction: column; gap: 8px; }
  .contact-item {
    display: flex; align-items: center; gap: 9px;
    font-size: 13px; color: var(--slate); white-space: nowrap;
  }
  .contact-icon { width: 14px; height: 14px; flex: none; }
  .contact-icon .ic-fill { fill: var(--mauve); }
  .contact-icon .ic-line { fill: none; stroke: var(--mauve); stroke-width: 1.6; }
</style>
</head>
<body>
<main class="sheet">

  <section class="card card-front" aria-label="Business card front">
    <div class="front-brand">
      <span class="brand-dot"></span>
      <span class="brand-name">RW Office Partners</span>
    </div>
    <svg class="card-band" viewBox="0 0 540 40" preserveAspectRatio="none" aria-hidden="true">
      <polygon class="band-accent" points="320,26 540,10 540,40 310,40"/>
      <polygon class="band-main" points="0,30 330,26 318,40 0,40"/>
    </svg>
  </section>

  <section class="card card-back" aria-label="Business card back">
    <div class="back-layout">
      <div class="back-brand">
        <div class="brand-name">RW Office Partners</div>
        <div class="tagline">Your tidy answer finder</div>
      </div>
      <span class="divider"></span>
      <ul class="contact-list">
        <li class="contact-item">
          <svg class="contact-icon" viewBox="0 0 14 14" aria-hidden="true"><rect class="ic-line" x="3.5" y="1" width="7" height="12" rx="1.5"/></svg>
          61 487 902 346
        </li>
        <li class="contact-item">
          <svg class="contact-icon" viewBox="0 0 14 14" aria-hidden="true"><rect class="ic-fill" x="1" y="1" width="12" height="12" rx="2"/></svg>
          @rwofficepartners
        </li>
        <li class="contact-item">
          <svg class="contact-icon" viewBox="0 0 14 14" aria-hidden="true"><circle class="ic-fill" cx="7" cy="7" r="6"/></svg>
          @rwofficepartners
        </li>
        <li class="contact-item">
          <svg class="contact-icon" viewBox="0 0 14 14" aria-hidden="true"><rect class="ic-line" x="1" y="3" width="12" height="8"/><polyline class="ic-line" points="1,3 7,8 13,3"/></svg>
          marisol@rwofficepartners.com.au
        </li>
        <li class="contact-item">
          <svg class="contact-icon" viewBox="0 0 14 14" aria-hidden="true"><circle class="ic-line" cx="7" cy="7" r="5.5"/><ellipse class="ic-line" cx="7" cy="7" rx="2.4" ry="5.5"/><line class="ic-line" x1="1.5" y1="7" x2="12.5" y2="7"/></svg>
          www.rwofficepartners.com.au
        </li>
      </ul>
    </div>
    <svg class="card-band" viewBox="0 0 540 40" preserveAspectRatio="none" aria-hidden="true">
      <polygon class="band-accent" points="320,26 540,10 540,40 310,40"/>
      <polygon class="band-main" points="0,30 330,26 318,40 0,40"/>
    </svg>
  </section>

</main>
</body>
</html>
```